Business card for Sports Apparel business

DOUBLE SIDED DESIGN
We need business cards for a new sports apparel business. We are developing a protective headband for soccer initially.
Corvell is focused on designing and developing head protection products to reduce the likelihood of concussion when playing sports. Exploring and understanding medical insights, material science research, current and former players experiences and governing bodies guidelines has allowed Corvell to develop the safety, style, form and function requirements of a suitable product to bring to market.
Target Market(s)
Mums buying kits for the sons and daughters. Amateur footballers.
Industry/Entity Type
Sporting Good
Contact Information for Business Card
Martin Ashgrove - CEO
Mobile: +44 7391608254
Email: martin@corvell.co.uk
Tel: 0208 5143927
Helena Pardoe - COO
Mob: +44 7356 409183
Email: helena@corvell.co.uk
Tel: 0208 5143927
Duncan Wyvern - CCO
Mob: +44 7468 230517
Email: duncan@corvell.co.uk
Tel: 0208 5143927
Look and feel

```html
<!DOCTYPE html>
<html lang="en">
<head>
<meta charset="utf-8">
<title>Corvell Business Card</title>
<link href="https://fonts.googleapis.com/css2?family=Montserrat:wght@400;500;600&display=swap" rel="stylesheet">
<style>
  :root {
    --backdrop: #e4e4e4;
    --card-white: #ffffff;
    --card-dark: #4a4a4c;
    --brand-blue: #0d4a86;
    --ink: #2f2f2f;
    --emboss: #3e3e40;
  }
  * { margin: 0; padding: 0; box-sizing: border-box; }
  html, body {
    width: 1200px;
    height: 800px;
    overflow: hidden;
    background: var(--backdrop);
    font-family: "Montserrat", sans-serif;
  }
  .sheet {
    width: 1200px;
    height: 800px;
    display: flex;
    align-items: center;
    justify-content: center;
    gap: 40px;
  }
  .card {
    position: relative;
    width: 540px;
    height: 309px;
    border-bottom: 3px solid var(--brand-blue);
  }
  .card-front { background: var(--card-white); }
  .card-back {
    background: var(--card-dark);
    display: flex;
    align-items: center;
    justify-content: center;
  }
  .brand-name {
    font-weight: 600;
    letter-spacing: 4px;
    text-transform: uppercase;
  }
  .card-front .brand-name {
    position: absolute;
    top: 42px;
    right: 40px;
    font-size: 40px;
    color: var(--brand-blue);
  }
  .card-back .brand-name {
    font-size: 52px;
    color: var(--emboss);
  }
  .holder {
    position: absolute;
    left: 34px;
    top: 150px;
  }
  .holder-name {
    font-size: 19px;
    font-weight: 500;
    color: var(--brand-blue);
    text-transform: uppercase;
    letter-spacing: 0.5px;
  }
  .holder-role {
    font-size: 11px;
    color: var(--ink);
    margin-top: 2px;
  }
  .divider {
    position: absolute;
    left: 34px;
    top: 200px;
    width: 440px;
    height: 1px;
    background: var(--brand-blue);
  }
  .contacts {
    position: absolute;
    left: 34px;
    top: 214px;
    list-style: none;
  }
  .contacts li {
    display: flex;
    align-items: center;
    gap: 8px;
    font-size: 12px;
    color: var(--ink);
    line-height: 20px;
  }
  .contacts svg { width: 11px; height: 11px; flex: none; }
  .website {
    position: absolute;
    right: 34px;
    bottom: 30px;
    font-size: 11px;
    color: var(--ink);
  }
</style>
</head>
<body>
<main class="sheet">
  <section class="card card-front">
    <div class="brand-name">Corvell</div>
    <div class="holder">
      <div class="holder-name">Martin Ashgrove</div>
      <div class="holder-role">CEO</div>
    </div>
    <div class="divider"></div>
    <ul class="contacts">
      <li>
        <svg viewBox="0 0 12 12" aria-hidden="true"><path d="M2.5 1 L4.5 1 L5 3.5 L3.8 4.4 Q5 7 7.6 8.2 L8.5 7 L11 7.5 L11 9.5 Q10.5 11 9 11 Q1 10 1 2.5 Q1 1 2.5 1 Z" fill="var(--brand-blue)"/></svg>
        0208 5143927
      </li>
      <li>
        <svg viewBox="0 0 12 12" aria-hidden="true"><rect x="3" y="0.8" width="6" height="10.4" rx="1" fill="none" stroke="var(--brand-blue)" stroke-width="1.2"/><circle cx="6" cy="9.5" r="0.6" fill="var(--brand-blue)"/></svg>
        +44 7391608254
      </li>
      <li>
        <svg viewBox="0 0 12 12" aria-hidden="true"><rect x="0.5" y="2" width="11" height="8" fill="var(--brand-blue)"/><path d="M0.5 2 L6 6.5 L11.5 2" fill="none" stroke="#fff" stroke-width="1"/></svg>
        martin@corvell.co.uk
      </li>
    </ul>
    <div class="website">www.corvell.co.uk</div>
  </section>

  <section class="card card-back">
    <div class="brand-name">Corvell</div>
  </section>
</main>
</body>
</html>
```